Word Doc Report NEED THIS OVERNIGHT!

I have a design ready, I need someone to take a report that we have, and input it in to the design that has been created. The final product needs to be delivered in Word.
The file called "Sketch Forge" is the design concept we need to use
The file called "7 Elmwick Lane" is all of the data that needs to be put into the word doc based on the elements in the Sketch Forge file.

```html
<!DOCTYPE html>
<html lang="en">
<head>
<meta charset="utf-8">
<title>ACT Maintenance Plan – Report Layout</title>
<link rel="stylesheet" href="https://fonts.googleapis.com/css2?family=Arimo:wght@400;700&family=Lato:wght@400;700&family=Questrial&display=swap">
<style>
  :root {
    --backdrop: #d3dcdb;
    --paper: #ffffff;
    --navy: #0d1a80;
    --sky: #3fa9f5;
    --mint: #5be39f;
    --ink: #1b1b1b;
    --rule: #d6d6d6;
    --callout: #4aa8f0;
  }
  * { box-sizing: border-box; margin: 0; padding: 0; }
  html, body { width: 1200px; height: 1200px; overflow: hidden; }
  body { background: var(--backdrop); position: relative; font-family: "Lato", sans-serif; color: var(--ink); }

  .page { position: absolute; top: 234px; width: 517px; height: 732px; background: var(--paper); overflow: hidden; }
  .cover { left: 66px; }
  .summary { left: 618px; }

  /* Cover */
  .cover-photo { position: absolute; left: 0; top: 0; width: 517px; height: 330px;
    background: linear-gradient(180deg, #5ea6ef 0%, #b9c7d9 50%, #c49067 80%, #6b6149 100%); }
  .cover-graphic { position: absolute; left: 0; top: 300px; width: 517px; height: 330px;
    background: linear-gradient(160deg, var(--navy) 0%, var(--navy) 62%, #1c47a8 82%, var(--mint) 100%); }
  .brand { position: absolute; left: 40px; top: 90px; display: flex; align-items: center; gap: 8px;
    font-family: "Questrial", sans-serif; font-size: 27px; color: var(--navy); }
  .brand-dot { width: 12px; height: 12px; border-radius: 50%; background: var(--navy); }
  .cover-title { position: absolute; left: 37px; top: 370px; font-family: "Arimo", sans-serif; font-weight: 700;
    font-size: 29px; line-height: 43px; }
  .cover-title .t-act { color: var(--sky); }
  .cover-title .t-maint { color: var(--mint); }
  .cover-title .t-plan { color: #fff; }
  .cover-rule { position: absolute; left: 37px; top: 510px; width: 212px; height: 1px; background: #fff; }
  .cover-date { position: absolute; left: 37px; top: 520px; font-family: "Questrial", sans-serif; font-size: 15.5px; color: #fff; }
  .cover-foot { position: absolute; font-family: "Questrial", sans-serif; font-size: 11px; line-height: 19px; color: var(--ink); }
  .foot-site { left: 27px; top: 680px; font-size: 12.5px; line-height: 15px; }
  .foot-contact { left: 228px; top: 652px; }
  .foot-address { left: 395px; top: 652px; }
  .foot-address strong { font-family: "Arimo", sans-serif; font-weight: 700; }

  /* Summary page */
  .summary .h-main { position: absolute; left: 30px; top: 50px; font-size: 21px; font-weight: 700; color: var(--sky); letter-spacing: .2px; }
  .facts { position: absolute; left: 30px; top: 0; width: 235px; }
  .fact { position: absolute; left: 0; width: 235px; font-size: 8px; line-height: 11px; }
  .fact-label { position: absolute; left: 0; top: 0; text-transform: uppercase; letter-spacing: .2px; }
  .fact-label.blue { color: var(--sky); }
  .fact-label.green { color: #2fc98a; }
  .fact-value { position: absolute; left: 120px; top: 0; width: 95px; padding-bottom: 3px; border-bottom: 1px solid var(--rule); }

  .h-sub { position: absolute; font-size: 14.5px; font-weight: 700; color: var(--sky); }
  .body-text { position: absolute; font-size: 8.6px; line-height: 11.7px; text-align: justify; }
  .body-text p + p { margin-top: 11px; }
  .bullets { list-style: none; }
  .bullets li { position: relative; padding-left: 14px; }
  .bullets li::before { content: ""; position: absolute; left: 2px; top: 4px; width: 3px; height: 3px; border-radius: 50%; background: #2fc98a; }

  .callout { position: absolute; left: 267px; top: 462px; width: 216px; height: 138px; background: var(--callout);
    color: #fff; padding: 9px 7px; font-size: 7.4px; line-height: 11.5px; }
  .callout strong { font-size: 8.4px; }
  .signature { position: absolute; left: 274px; top: 626px; width: 160px; height: 30px;
    background: linear-gradient(90deg, #f1f1f1, #e8e8e8); }
  .signer { position: absolute; left: 274px; top: 669px; font-family: "Arimo", sans-serif; font-weight: 700; font-size: 10px; line-height: 12.5px; }
  .page-num { position: absolute; left: 484px; top: 691px; font-size: 7.6px; font-weight: 700; }
</style>
</head>
<body>

<section class="page cover">
  <div class="cover-photo" role="img" aria-label="Photo of a multi-storey apartment building at dusk with trees in front"></div>
  <div class="cover-graphic" role="img" aria-label="Decorative geometric band graphic in navy, mint and sky blue"></div>

  <div class="brand"><span class="brand-dot"></span>Dwelling Notes</div>

  <h1 class="cover-title">
    <span class="t-act">ACT</span><br>
    <span class="t-maint">Maintenance</span><br>
    <span class="t-plan">Plan</span>
  </h1>
  <div class="cover-rule"></div>
  <div class="cover-date">2 May 2022</div>

  <div class="cover-foot foot-site">Units Plan1722<br>7 Elmwick Lane Canberra City</div>
  <div class="cover-foot foot-contact">p 6100 0199<br>dwellingnotes.com.au<br>hello@dwellingnotes.com.au</div>
  <div class="cover-foot foot-address"><strong>Address</strong><br>14 Larkfield Road<br>Ashbury ACT 2611</div>
</section>

<section class="page summary">
  <h2 class="h-main">REPORT SUMMARY</h2>

  <div class="facts">
    <div class="fact" style="top:87px"><span class="fact-label blue">Client</span><span class="fact-value">Harbourline Strata Pty Ltd</span></div>
    <div class="fact" style="top:115px"><span class="fact-label green">Building Location</span><span class="fact-value">7 Elmwick Lane Canberra City ACT</span></div>
    <div class="fact" style="top:150px"><span class="fact-label blue">Block Number</span><span class="fact-value">13</span></div>
    <div class="fact" style="top:168px"><span class="fact-label green">Section Number</span><span class="fact-value">12</span></div>
    <div class="fact" style="top:189px"><span class="fact-label blue">Scheme Number</span><span class="fact-value">UP1722</span></div>
    <div class="fact" style="top:208px"><span class="fact-label green">Inspection Date</span><span class="fact-value">2 May 2022</span></div>
    <div class="fact" style="top:223px"><span class="fact-label blue">Inspector</span><span class="fact-value">Lena Corvell</span></div>
    <div class="fact" style="top:237px"><span class="fact-label green">Weather Conditions</span><span class="fact-value">Fine</span></div>
    <div class="fact" style="top:258px"><span class="fact-label blue">Reference Number</span><span class="fact-value">35TST</span></div>
  </div>

  <h3 class="h-sub" style="left:34px; top:302px;">Building Class</h3>
  <ul class="body-text bullets" style="left:32px; top:323px; width:205px;">
    <li>Residential Units are Class A</li>
  </ul>

  <div class="body-text" style="left:34px; top:347px; width:203px;">
    <p>In typical Class A Units Plans, the unit owner owns the inside of the unit but not the main structure of the building. Usually, the individual owner owns from the inside of their lot to halfway out through the boundary walls, ceiling, and the floor. In general, the Owners Corporation owns the walls, ceiling and floor from outside of the lot to halfway in. The internal walls within the unit (e.g. the wall between the kitchen and lounge room), floor coverings, light fittings and curtains are all the property of the unit owner.</p>
    <p>The Unit Titles (Management) Act 2011 and associated regulations provides the framework for the management of multi-unit residential properties. All Owners Corporations are required to hold a Maintenance Plan, considering the Developers Maintenance Schedule (if available). The Executive Committee then references this plan as part of their responsibility for overseeing the maintenance of the common property. The Owners Corporation should regularly review their</p>
  </div>

  <div class="body-text" style="left:34px; top:674px; width:203px; text-align:left;">
    <p>Thank you for the opportunity to work with you on this project, please do not hesitate to contact our team.</p>
  </div>

  <div class="body-text" style="left:274px; top:48px; width:202px;">
    <p>maintenance plan and amend when necessary. A comprehensive database relating to the maintenance, repair or replacement undertaken to systems, equipment, structures and other items on the common property, including copies of manuals and warranties (where available) has been compiled for this building.</p>
    <p>Following the preparation of our project file for 7 Elmwick Lane Canberra which included referencing materials such as maintenance schedules, sinking fund reports, warranties, manufacturer’s recommendations, and specific product information provided to us, our Building Inspector conducted a comprehensive on-site visual inspection on 2 May 2022. It is critical that this Maintenance Plan is monitored and updated on an ongoing basis to ensure the optimum working condition of systems, equipment, structures and other elements of the common property and to avoid costly reactive repairs.</p>
  </div>

  <h3 class="h-sub" style="left:274px; top:330px;">Project Scope:</h3>
  <div class="body-text" style="left:274px; top:352px; width:202px;">
    <p>This Maintenance Plan has been compiled to assist the Owners Corporation and Strata Managers to meet their obligations with respect to the following legislation (both as amended 1 November 2020):</p>
    <ul class="bullets" style="margin-top:3px; padding-left:12px;">
      <li>Unit Titles (Management) Act 2011 (s24);</li>
      <li>Unit Titles (Management) Regulation 2011 (s4A)</li>
    </ul>
  </div>

  <div class="callout">
    <strong>IMPORTANT:</strong> This report is intended to be read in its entirety. It has been commissioned to satisfy the requirements of 4A Maintenance plan – Act, s 24 (3), Unit Titles Management Regulation 2011. The appropriate Strata Group Representative or Members of the Body Corporate Executive are requested to immediately contact our company if any of the report’s content is not fully understood and requires clarification or further explanation. <strong style="font-size:7.4px;">Please refer to important Scope and Limitations at the end of this document.</strong>
  </div>

  <div class="signature" role="img" aria-label="Handwritten signature of the inspector"></div>
  <div class="signer">Lena Corvell<br>Senior Building Inspector</div>
  <div class="page-num">1</div>
</section>

</body>
</html>
```